Business Card Upgrade

I have designed our business card using our new logo. I think it needs imporovements. We used to have two cards for our business. One card was for our software business, and the other was for our consulting business. We are now in the process of combining our websites, marketing, name, and a new logo.

Our goal is to have a really sharp professional logo. One reason I designed the card the way I did was that our Titles are sometimes long, and by separating the person's name and title, it shows up very well and the title can be adjusted no matter how long it is. Sometimes the title can be 4 or 5 words or more.

We really like our logo on black as it shows up very nice. Our PMS colors are as follows: 368C and 459C.

The Designer that will be working with us will need to deliver the following:

The front and back of the Business Card Design will need to be delivered in a high quality JPEG, and
The front and back of the Business Card Design in Illustrator Format .ai
Any fonts will need to be sent to us if they are not standard and are required to open the Illustrator file correctly.

To help us get a good idea of the card with a title, please use the title: " Director of Software Development "

NOTE: The chosen designer will be selected to design our new letterhead within 2 weeks from the closing of this contest.

To help us make sure the card design works with longer titles, please use the followign job title on the card:  

"Director of Software and Product Development"

 

ALL DESIGNERS:

1. I appreciate the different angles you are showing the cards, but please be sure and always show the direct view, so I can see the layout and what the person I hand the card will see.

2. Please do not use white.  Please use off white as I don't care for white cards and they get dirty easy and do not represent the designs well.

Dear Designers,

Please provide samples straight one as a viewer of the card will see.  Some of the angles that are presented make it impossible to tell how everything fits, and sometimes even makes areas look skewed. So, please provide a straight sample view.

Pinnacle 400 company executives such as Vice Presidents, and Directors

Software

• Professional looking Card.

Our customers are Directors, Vice Presidents, and Presidents of companies as large as Pinnacle 400 companies. The card needs to get attention wile still looking professional.

Delivery of the finished product in Illustrator Format with any fonts needed to edit the text or open the file.

The card will be a heavy stock with a soft touch coating for that silk feel.

```html
<!DOCTYPE html>
<html lang="en">
<head>
<meta charset="utf-8">
<title>Meridian Trade Group – Business Card</title>
<link href="https://fonts.googleapis.com/css2?family=Montserrat:wght@400;600;800&display=swap" rel="stylesheet">
<style>
  :root {
    --stage: #e9e6df;
    --card-black: #0b0b0b;
    --card-charcoal: #1c1c1c;
    --brand-green: #5cc84a;
    --brand-green-deep: #2f9e32;
    --brand-cream: #e6d79a;
    --text-light: #f4f1e8;
    --text-muted: #bdb9ae;
  }
  html, body {
    margin: 0;
    padding: 0;
    width: 1200px;
    height: 720px;
    overflow: hidden;
    background: var(--stage);
    font-family: "Montserrat", Arial, sans-serif;
  }
  .canvas {
    position: relative;
    width: 1200px;
    height: 720px;
    display: flex;
    align-items: center;
    justify-content: center;
    gap: 40px;
  }
  .card {
    position: relative;
    width: 540px;
    height: 309px;
    border-radius: 6px;
    overflow: hidden;
    background: linear-gradient(160deg, var(--card-charcoal) 0%, var(--card-black) 60%);
    box-shadow: 0 10px 28px rgba(0,0,0,0.22);
  }
  .card-shapes {
    position: absolute;
    inset: 0;
    width: 100%;
    height: 100%;
  }
  .brand-name {
    position: absolute;
    margin: 0;
    color: var(--brand-green-deep);
    font-weight: 600;
    text-transform: uppercase;
    line-height: 1.05;
  }
  .card-front .brand-name {
    left: 150px;
    top: 120px;
    font-size: 30px;
    letter-spacing: 3px;
    transform: rotate(-14deg);
    transform-origin: left top;
  }
  .card-back .brand-name {
    left: 16px;
    top: 248px;
    font-size: 13px;
    letter-spacing: 1.5px;
  }
  .person {
    position: absolute;
    left: 300px;
    top: 58px;
    color: var(--text-light);
  }
  .person-name {
    margin: 0;
    font-size: 26px;
    font-weight: 800;
    letter-spacing: 0.5px;
  }
  .person-title {
    margin: 4px 0 0;
    font-size: 7px;
    font-weight: 600;
    letter-spacing: 0.6px;
    text-transform: uppercase;
    color: var(--text-muted);
  }
  .contact-list {
    list-style: none;
    margin: 22px 0 0;
    padding: 0;
  }
  .contact-item {
    display: flex;
    align-items: center;
    gap: 9px;
    font-size: 11.5px;
    font-weight: 400;
    margin-bottom: 9px;
    color: var(--text-light);
  }
  .contact-icon {
    width: 14px;
    height: 14px;
    flex: none;
  }
</style>
</head>
<body>
<main class="canvas">

  <section class="card card-front" aria-label="Card front">
    <svg class="card-shapes" viewBox="0 0 540 309" aria-hidden="true">
      <defs>
        <linearGradient id="frontGreen" x1="0" y1="0" x2="1" y2="1">
          <stop offset="0" stop-color="#6fd85a"/>
          <stop offset="1" stop-color="#3fb23a"/>
        </linearGradient>
      </defs>
      <path d="M0 95 C160 95 360 70 540 0 L540 175 C430 200 300 250 210 309 L0 309 Z" fill="url(#frontGreen)"/>
      <path d="M0 95 C160 95 360 70 540 0" fill="none" stroke="var(--brand-cream)" stroke-width="7"/>
      <path d="M540 175 C430 200 300 250 210 309" fill="none" stroke="var(--brand-cream)" stroke-width="7"/>
    </svg>
    <p class="brand-name">Meridian<br>Trade Group</p>
  </section>

  <section class="card card-back" aria-label="Card back">
    <svg class="card-shapes" viewBox="0 0 540 309" aria-hidden="true">
      <defs>
        <linearGradient id="backGreen" x1="0" y1="0" x2="1" y2="1">
          <stop offset="0" stop-color="#6fd85a"/>
          <stop offset="1" stop-color="#3fb23a"/>
        </linearGradient>
      </defs>
      <path d="M0 215 C80 205 160 240 190 309 L0 309 Z" fill="url(#backGreen)"/>
      <path d="M0 215 C80 205 160 240 190 309" fill="none" stroke="var(--brand-cream)" stroke-width="6"/>
    </svg>
    <p class="brand-name">Meridian<br>Trade Group</p>

    <div class="person">
      <h1 class="person-name">YOUR NAME</h1>
      <p class="person-title">Director of Software and Product Development</p>
      <ul class="contact-list">
        <li class="contact-item">
          <svg class="contact-icon" viewBox="0 0 14 14" aria-hidden="true"><path d="M3 1.5 L5 1.5 L6 4.5 L4.6 5.5 C5.3 7 6.8 8.6 8.5 9.4 L9.5 8 L12.5 9 L12.5 11 C12.5 12 11.6 12.6 10.6 12.5 C5.8 12 2 8.2 1.5 3.4 C1.4 2.4 2 1.5 3 1.5 Z" fill="var(--brand-green)"/></svg>
          0423-555-017
        </li>
        <li class="contact-item">
          <svg class="contact-icon" viewBox="0 0 14 14" aria-hidden="true"><circle cx="7" cy="7" r="6" fill="none" stroke="var(--brand-green)" stroke-width="1.4"/><path d="M1 7 H13 M7 1 C4 4 4 10 7 13 M7 1 C10 4 10 10 7 13" fill="none" stroke="var(--brand-green)" stroke-width="1.1"/></svg>
          www.meridiantrade.com
        </li>
        <li class="contact-item">
          <svg class="contact-icon" viewBox="0 0 14 14" aria-hidden="true"><rect x="1" y="3" width="12" height="8.5" rx="1" fill="var(--brand-green)"/><path d="M1.5 3.8 L7 8 L12.5 3.8" fill="none" stroke="var(--card-black)" stroke-width="1.1"/></svg>
          hello@meridiantrade.com
        </li>
        <li class="contact-item">
          <svg class="contact-icon" viewBox="0 0 14 14" aria-hidden="true"><path d="M7 13 C7 13 2.5 8 2.5 5.3 A4.5 4.5 0 0 1 11.5 5.3 C11.5 8 7 13 7 13 Z" fill="var(--brand-green)"/><circle cx="7" cy="5.3" r="1.7" fill="var(--card-black)"/></svg>
          your address will be here
        </li>
      </ul>
    </div>
  </section>

</main>
</body>
</html>
```